construction company business card

I need a business card design for a new company called TK CREST WORKS. I'd like to see different designs with the name tk CREST WORKS, and others for TK Crest Works. The company field is Home Improvement and everything related with construction. Colors I like are red, blue and black. The final design should communicate/show simplicity and security.

Industry/Entity Type

Construction

Contact Information for Business Card

TK CREST WORKS
Tobias Kellner
(917)555-0143
57-31 226th Avenue
Harbor Glen
11562, NY

Requirements
Must have
• HOME IMPROVEMENT

```html
<!DOCTYPE html>
<html lang="en">
<head>
<meta charset="utf-8">
<title>TK Crest Works – Business Card</title>
<link rel="stylesheet" href="https://fonts.googleapis.com/css2?family=Noto+Serif:wght@400&display=swap">
<style>
  :root {
    --backdrop: #6e5a4a;
    --card-edge: #3a4ea6;
    --card-glow: #05aeea;
    --card-mid: #2a7fd0;
    --ink: #0a0a12;
  }
  * { margin: 0; padding: 0; box-sizing: border-box; }
  html, body {
    width: 1200px;
    height: 700px;
    overflow: hidden;
  }
  body {
    background: var(--backdrop);
    font-family: "Noto Serif", Georgia, serif;
    color: var(--ink);
    position: relative;
  }
  .business-card {
    position: absolute;
    left: 180px;
    top: 110px;
    width: 840px;
    height: 480px;
    background: radial-gradient(ellipse 55% 60% at 50% 52%, var(--card-glow) 0%, var(--card-mid) 45%, var(--card-edge) 100%);
    display: flex;
    flex-direction: column;
    align-items: center;
    padding-top: 130px;
  }
  .brand {
    display: flex;
    align-items: center;
    gap: 16px;
  }
  .brand-mark {
    width: 26px;
    height: 26px;
    background: var(--ink);
  }
  .brand-name {
    font-size: 38px;
    font-weight: 400;
    letter-spacing: 0.5px;
  }
  .brand-rule {
    width: 440px;
    height: 8px;
    background: var(--ink);
    margin-top: 14px;
  }
  .tagline {
    font-size: 14px;
    margin-top: 6px;
  }
  .contact-heading {
    font-size: 40px;
    font-weight: 400;
    margin-top: 10px;
    line-height: 1.1;
  }
  .contact-details {
    font-style: normal;
    font-size: 18px;
    letter-spacing: 1.5px;
    text-align: center;
    margin-top: 12px;
    line-height: 1.4;
  }
</style>
</head>
<body>
  <section class="business-card">
    <div class="brand">
      <span class="brand-mark"></span>
      <span class="brand-name">TK Crest Works</span>
    </div>
    <div class="brand-rule"></div>
    <p class="tagline">Home Improvement and everything related with construction</p>
    <h1 class="contact-heading">Contact Information</h1>
    <address class="contact-details">
      TK Crest Works Tobias Kellner (917)555-0143 57-31<br>
      226th Avenue Harbor Glen 11562, NY
    </address>
  </section>
</body>
</html>
```